Manufacturing and engineering company needs corporate stationary

Looking for professional stationary to use internally as well as for giveaways for customers. Looking for digital and printed options.

The logo file attached has the overall colour scheme and the logo needs to be used in the stationary. The circle portion of the logo can be used independently. We are open to variations on the colours and style of logo but it should remain very similar to the attached.

Font styles to use
Serif
Sans Serif

Requirements
Must have
• The logo or at the very least the circle portion of the logo
Nice to have
• Would like a powerpoint template, word document template for proposals, printed brochure template
Should not have
• Business cards are not the focus, while you can suggest ideas this is not the focus

```html
<!DOCTYPE html>
<html lang="en">
<head>
<meta charset="utf-8">
<title>Norvale Stationery</title>
<link href="https://fonts.googleapis.com/css2?family=Arimo:wght@400;700&display=swap" rel="stylesheet">
<style>
  :root{
    --maroon:#4d090c;
    --gold:#c4a05a;
    --grey:#8a8a8a;
    --ink:#555;
    --paper:#ffffff;
    --backdrop:#eceeef;
  }
  *{box-sizing:border-box;margin:0;padding:0}
  html,body{width:1200px;height:953px;overflow:hidden}
  body{background:var(--backdrop);font-family:"Arimo",Arial,sans-serif;color:var(--ink);position:relative}

  .letterhead{position:absolute;left:80px;top:90px;width:520px;height:673px;background:var(--paper);box-shadow:0 6px 18px rgba(0,0,0,.12)}
  .brand{display:flex;align-items:center;gap:8px;position:absolute}
  .brand-dot{border-radius:50%;border:3px solid var(--grey)}
  .brand-name{font-weight:700;color:var(--grey)}
  .letterhead .brand{left:40px;top:44px}
  .letterhead .brand-dot{width:38px;height:38px}
  .letterhead .brand-name{font-size:22px}

  .tagline{position:absolute;right:48px;top:40px;border-left:1px solid var(--maroon);padding-left:14px;font-size:10px;line-height:13px;color:var(--grey)}

  .lh-contact{position:absolute;right:30px;bottom:44px;display:flex;gap:26px;font-size:7.5px;line-height:11px;color:var(--grey)}
  .lh-contact .row{display:flex;gap:5px;align-items:flex-start}
  .icon{width:8px;height:8px;flex:none;margin-top:1px;fill:var(--grey)}
  .band{position:absolute;left:0;bottom:0;width:100%;height:28px;display:block}

  .card{position:absolute;width:440px;height:252px;box-shadow:0 6px 18px rgba(0,0,0,.12)}
  .card-back{left:690px;top:150px;background:var(--maroon)}
  .card-back .brand{left:50%;top:50%;transform:translate(-50%,-50%);flex-direction:column;gap:10px}
  .card-back .brand-dot{width:74px;height:74px;border-color:var(--paper)}
  .card-back .brand-name{color:var(--paper);font-size:26px}

  .card-front{left:690px;top:470px;background:var(--paper)}
  .card-front .brand{left:28px;top:30px}
  .card-front .brand-dot{width:32px;height:32px}
  .card-front .brand-name{font-size:19px}
  .person{position:absolute;left:28px;top:150px}
  .person-name{font-weight:700;color:var(--maroon);font-size:15px}
  .person-title{font-size:9px;color:var(--ink);margin-top:3px}
  .card-contact{position:absolute;right:24px;top:30px;font-size:9px;line-height:12px;color:var(--ink);text-align:right}
  .card-contact .row{display:flex;justify-content:flex-end;gap:8px;margin-bottom:8px}
  .card-contact .icon{width:9px;height:9px;fill:var(--maroon)}
</style>
</head>
<body>

<section class="letterhead">
  <div class="brand"><span class="brand-dot"></span><span class="brand-name">Norvale</span></div>
  <div class="tagline">Manufacturing<br>Engineering</div>

  <div class="lh-contact">
    <div class="col">
      <div class="row"><svg class="icon" viewBox="0 0 10 10"><path d="M5 0a3.5 3.5 0 0 0-3.5 3.5C1.5 6 5 10 5 10s3.5-4 3.5-6.5A3.5 3.5 0 0 0 5 0zm0 5a1.4 1.4 0 1 1 0-2.8A1.4 1.4 0 0 1 5 5z"/></svg>
        <span>Address:<br>4815 - 52 Ave SE<br>Calgary, AB<br>T2C 3R7</span></div>
      <div class="row"><svg class="icon" viewBox="0 0 10 10"><circle cx="5" cy="5" r="4.5"/></svg><span>Website: www.norvale.ca</span></div>
    </div>
    <div class="col">
      <div class="row"><svg class="icon" viewBox="0 0 10 10"><path d="M2 0l2 2.5-1 1.2a6 6 0 0 0 3.3 3.3l1.2-1L10 8l-1.5 2C4 10 0 6 0 1.5z"/></svg><span>Phone: (403) 555-0142</span></div>
      <div class="row"><svg class="icon" viewBox="0 0 10 10"><rect x="0" y="3" width="10" height="5"/><rect x="2" y="0" width="6" height="3"/></svg><span>Fax: (403) 555-0187</span></div>
      <div class="row"><svg class="icon" viewBox="0 0 10 10"><path d="M0 2h10v6H0z"/></svg><span>Email: sales@norvale.ca</span></div>
    </div>
  </div>

  <svg class="band" viewBox="0 0 520 28" preserveAspectRatio="none"><polygon points="0,20 300,20 312,10 490,10 500,0 520,0 520,28 0,28" fill="var(--maroon)"/></svg>
</section>

<section class="card card-back">
  <div class="brand"><span class="brand-dot"></span><span class="brand-name">Norvale</span></div>
</section>

<section class="card card-front">
  <div class="brand"><span class="brand-dot"></span><span class="brand-name">Norvale</span></div>

  <div class="card-contact">
    <div class="row"><span>4815 - 52 Ave SE<br>Calgary, AB<br>T2C 3R7</span><svg class="icon" viewBox="0 0 10 10"><path d="M5 0a3.5 3.5 0 0 0-3.5 3.5C1.5 6 5 10 5 10s3.5-4 3.5-6.5A3.5 3.5 0 0 0 5 0zm0 5a1.4 1.4 0 1 1 0-2.8A1.4 1.4 0 0 1 5 5z"/></svg></div>
    <div class="row"><span>(403) 555-0142</span><svg class="icon" viewBox="0 0 10 10"><path d="M2 0l2 2.5-1 1.2a6 6 0 0 0 3.3 3.3l1.2-1L10 8l-1.5 2C4 10 0 6 0 1.5z"/></svg></div>
    <div class="row"><span>(403) 555-0187</span><svg class="icon" viewBox="0 0 10 10"><rect x="0" y="3" width="10" height="5"/><rect x="2" y="0" width="6" height="3"/></svg></div>
    <div class="row"><span>sales@norvale.ca</span><svg class="icon" viewBox="0 0 10 10"><path d="M0 2h10v6H0z"/></svg></div>
    <div class="row"><span>www.norvale.ca</span><svg class="icon" viewBox="0 0 10 10"><circle cx="5" cy="5" r="4.5"/></svg></div>
  </div>

  <div class="person">
    <div class="person-name">Daniel Harrow, P.Eng.</div>
    <div class="person-title">Board Chair and CEO</div>
  </div>

  <svg class="band" viewBox="0 0 440 28" preserveAspectRatio="none"><polygon points="0,22 180,22 192,12 320,12 330,4 440,4 440,28 0,28" fill="var(--maroon)"/></svg>
</section>

</body>
</html>
```